NEW YORK Plumbing/utility company 10 year anniversary business card

Looking For simple back and front business card would like to include a few things in description
We offer 24/7 emergency service
residential
commercial
industrial
municipal
services offered
Plumbing
hydro excavation
hydro jetting
Well pumps
Sewer pumps
water mains
sewer mains

```html
<!DOCTYPE html>
<html lang="en">
<head>
<meta charset="utf-8">
<title>Ridgeline Water &amp; Sewer – Business Card</title>
<link href="https://fonts.googleapis.com/css2?family=Montserrat:ital,wght@0,400;0,500;0,600;1,500&display=swap" rel="stylesheet">
<style>
  :root {
    --brand-blue: #1565a8;
    --brand-red: #e32326;
    --ink: #1f2a36;
    --paper: #ffffff;
    --backdrop: #e4e3e4;
  }
  * { box-sizing: border-box; margin: 0; padding: 0; }
  html, body {
    width: 1200px; height: 991px; overflow: hidden;
    background: var(--backdrop);
    font-family: "Montserrat", Arial, sans-serif;
    color: var(--ink);
  }
  .sheet {
    position: relative; width: 1200px; height: 991px;
    display: flex; align-items: center; justify-content: center; gap: 48px;
  }
  .card {
    position: relative; width: 520px; height: 297px;
    background: var(--paper);
    box-shadow: 0 6px 18px rgba(0,0,0,0.12);
    overflow: hidden;
  }
  /* front */
  .brand {
    position: absolute; left: 0; right: 0; top: 62px;
    display: flex; align-items: center; justify-content: center; gap: 12px;
  }
  .brand-dot { width: 20px; height: 20px; border-radius: 50%; background: var(--brand-red); }
  .brand-name {
    font-weight: 600; color: var(--brand-blue);
    font-size: 30px; line-height: 1.05; letter-spacing: 0.5px; text-transform: uppercase;
  }
  .brand-name small { display: block; font-size: 18px; letter-spacing: 3px; }
  .service-band {
    position: absolute; left: 0; right: 0; bottom: 0; height: 105px;
    background: var(--brand-blue); color: #fff; text-align: center;
    padding-top: 12px; font-size: 11.5px; line-height: 14.5px;
  }
  .service-band h3 { font-size: 11.5px; font-weight: 600; }
  .service-band p span { margin: 0 8px; }
  .service-band .gap { margin-top: 7px; }
  /* back */
  .rule { position: absolute; left: 0; top: 67px; width: 344px; height: 6px; background: var(--brand-blue); }
  .brand--small { left: auto; right: 30px; top: 44px; justify-content: flex-end; gap: 8px; }
  .brand--small .brand-dot { width: 11px; height: 11px; }
  .brand--small .brand-name { font-size: 14px; }
  .brand--small .brand-name small { font-size: 9px; letter-spacing: 1.8px; }
  .office {
    position: absolute; right: 350px; top: 164px; text-align: right;
    font-size: 12.5px; line-height: 15.5px;
  }
  .divider { position: absolute; left: 208px; top: 152px; width: 2px; height: 78px; background: var(--brand-blue); }
  .person { position: absolute; left: 240px; top: 158px; font-size: 15px; }
  .person .name { font-weight: 500; }
  .person .role { font-style: italic; font-weight: 500; font-size: 11.5px; margin-bottom: 6px; }
  .contact { display: flex; align-items: center; gap: 12px; font-size: 15px; line-height: 20px; }
  .contact svg { width: 12px; height: 12px; flex: none; }
  .website { position: absolute; left: 0; right: 0; top: 268px; text-align: center; font-size: 12.5px; font-weight: 500; }
  .website b { font-weight: 600; }
</style>
</head>
<body>
<main class="sheet">
  <section class="card card--front">
    <div class="brand">
      <span class="brand-dot"></span>
      <div class="brand-name">Ridgeline<small>Water &amp; Sewer</small></div>
    </div>
    <div class="service-band">
      <h3>We Offer 24/7 Emergency Service</h3>
      <p><span>Residential</span><span>Commercial</span><span>Industrial</span><span>Municipal</span></p>
      <h3 class="gap">Services Offered</h3>
      <p><span>Plumbing</span><span>Hydro Excavation</span><span>Hydro Jetting</span></p>
      <p><span>Well Pumps</span><span>Sewer Pumps</span><span>Water Mains</span><span>Sewer Mains</span></p>
    </div>
  </section>

  <section class="card card--back">
    <div class="rule"></div>
    <div class="brand brand--small">
      <span class="brand-dot"></span>
      <div class="brand-name">Ridgeline<small>Water &amp; Sewer</small></div>
    </div>
    <div class="office">
      Office:<br>Lorem Ipsum Street<br>Lorem, IP, 01234<br>888-888-8888
    </div>
    <div class="divider"></div>
    <div class="person">
      <p class="name">Name Lorem Ipsum</p>
      <p class="role">Director</p>
      <p class="contact">
        <svg viewBox="0 0 24 24" aria-hidden="true"><path fill="#1f2a36" d="M6.6 10.8a15.1 15.1 0 0 0 6.6 6.6l2.2-2.2c.3-.3.7-.4 1-.2 1.1.4 2.3.6 3.6.6.6 0 1 .4 1 1V20c0 .6-.4 1-1 1A17 17 0 0 1 3 4c0-.6.4-1 1-1h3.5c.6 0 1 .4 1 1 0 1.3.2 2.5.6 3.6.1.3 0 .7-.2 1z"/></svg>
        555-555-0808
      </p>
      <p class="contact">
        <svg viewBox="0 0 24 24" aria-hidden="true"><rect x="2.5" y="5" width="19" height="14" fill="none" stroke="#1f2a36" stroke-width="2"/><path d="M3 6l9 7 9-7" fill="none" stroke="#1f2a36" stroke-width="2"/></svg>
        Director@Loremopsum.com
      </p>
    </div>
    <p class="website"><b>Website:</b> Loremipsum.com</p>
  </section>
</main>
</body>
</html>
```